Poster of Insipirational Quotes

Attached is a list of leadership quotes from Harold Brenwick. I would like a poster made, incorporating whatever design elements you like, potentially including Harold's face, and one or more of the quotes. I intend to print this out in A3 or larger to hang on my wall.

The quotes are:

Being responsible sometimes means pissing people off.

The day soldiers stop bringing you their problems is the day you have stopped leading them.

Don't be buffaloed by experts and elites. Experts often possess more data than judgment. Elites can become so inbred that they produce hemophiliacs who bleed to death as soon as they are nicked by the real world.

Don't be afraid to challenge the pros, even in their own backyard.

Never neglect details. When everyone's mind is dulled or distracted the leader must be doubly vigilant.

You don't know what you can get away with until you try.

Keep looking below surface appearances. Don't shrink from doing so (just) because you might not like what you find.

Organization doesn't really accomplish anything. Plans don't accomplish anything, either. Theories of management don't much matter. Endeavors succeed or fail because of the people involved. Only by attracting the best people will you accomplish great deeds.

Organization charts and fancy titles count for next to nothing.

Never let your ego get so close to your position that when your position goes, your ego goes with it.

Fit no stereotypes. Don't chase the latest management fads. The situation dictates which approach best accomplishes the team's mission.

Perpetual optimism is a force multiplier.

Look for intelligence and judgment, and most critically, a capacity to anticipate, to see around corners. Also look for loyalty, integrity, a high energy drive, a balanced ego, and the drive to get things done.

Great leaders are almost always great simplifiers, who can cut through argument, debate and doubt, to offer a solution everybody can understand.

The commander in the field is always right and the rear echelon is wrong, unless proved otherwise.

Have fun in your command. Don't always run at a breakneck pace. Take leave when you've earned it: Spend time with your families. Corollary: surround yourself with people who take their work seriously, but not themselves, those who work hard and play hard.

Command is lonely.

Leadership is the art of accomplishing more than the science of management
says is possible.

I need to modify the specification based on the designs that I've seen.

Executive Office

Designer to choose colors to be used in the design.

• Quotes

```html
<!DOCTYPE html>
<html lang="en">
<head>
<meta charset="utf-8">
<title>Harold Brenwick – Quotes Poster</title>
<link rel="stylesheet" href="https://fonts.googleapis.com/css2?family=Jost:ital,wght@0,400;1,400&display=swap">
<style>
  :root {
    --bg: #000000;
    --ink: #ffffff;
    --photo-light: #8a8a86;
    --photo-mid: #55554f;
    --photo-dark: #242422;
    --portrait-light: #b9aea4;
    --portrait-dark: #1a1c24;
  }
  * { margin: 0; padding: 0; box-sizing: border-box; }
  html, body { width: 849px; height: 1200px; overflow: hidden; background: var(--bg); }
  .poster {
    position: relative;
    width: 849px;
    height: 1200px;
    background: var(--bg);
    color: var(--ink);
    font-family: "Jost", "Futura", sans-serif;
    overflow: hidden;
  }
  .quote {
    position: absolute;
    text-align: center;
    font-size: 34px;
    line-height: 40px;
    font-weight: 400;
    white-space: nowrap;
    transform: translateX(-50%);
  }
  .quote--dream   { left: 225px; top: 66px; }
  .quote--try     { left: 217px; top: 272px; }
  .quote--help    { left: 434px; top: 455px; }
  .quote--success { left: 437px; top: 589px; }
  .quote--leader  { left: 437px; top: 764px; }
  .quote--command { left: 437px; top: 926px; }

  .youth-photo {
    position: absolute;
    left: 455px;
    top: 0;
    width: 394px;
    height: 371px;
    background: linear-gradient(160deg, var(--photo-light) 0%, var(--photo-mid) 45%, var(--photo-dark) 100%);
  }
  .youth-photo__caption {
    position: absolute;
    left: 0;
    right: 0;
    bottom: 4px;
    text-align: center;
    font-size: 8.5px;
    line-height: 12px;
    text-transform: uppercase;
    letter-spacing: 0.1px;
    color: var(--ink);
  }

  .portrait {
    position: absolute;
    left: 0;
    top: 879px;
    width: 280px;
    height: 321px;
    background: radial-gradient(ellipse at 45% 30%, var(--portrait-light) 0%, var(--portrait-dark) 60%, var(--bg) 100%);
  }

  .signature {
    position: absolute;
    left: 437px;
    top: 1070px;
    transform: translateX(-50%);
    font-size: 38px;
    font-style: italic;
    font-weight: 400;
    white-space: nowrap;
    color: #f2f2f2;
  }
</style>
</head>
<body>
<main class="poster">
  <p class="quote quote--dream">“A dream doesn't become<br>reality through magic;<br>it takes sweat,<br>determination and hard work.”</p>

  <p class="quote quote--try">“You don't know<br>what you can get away with<br>until you try.”</p>

  <figure class="youth-photo" role="img" aria-label="Black and white photograph of young Harold Brenwick smiling in his ROTC uniform in front of a stone wall">
    <figcaption class="youth-photo__caption">Autumn 1954: Harold Brenwick in his ROTC uniform.<br>https://www.achievers-archive.org/profile/general-h-brenwick/</figcaption>
  </figure>

  <p class="quote quote--help">“Don't bother people for help<br>without first trying to solve the problem yourself.”</p>

  <p class="quote quote--success">“There are no secrets to success.<br>It is the result of<br>preparation, hard work, and learning from failure.”</p>

  <p class="quote quote--leader">“Leadership is the art of accomplishing more<br>than the science of management<br>says is possible.”</p>

  <p class="quote quote--command">“Command is lonely.”</p>

  <div class="portrait" role="img" aria-label="Portrait photograph of Harold Brenwick in later years, wearing glasses, a dark suit and striped tie"></div>

  <p class="signature">Harold Brenwick</p>
</main>
</body>
</html>
```